Portada libro no ficción: Rutas de empresa hacia lo Intangible

Busco diseño para libro de no ficción sobre los modelos de negocio del metaverso.

Maquetación de:
- Portada
- Contraportada
- Lomo

Requerimientos:
- Una portada única y creativa
- Portada para formato Lectoria, Vendalis y físico.
- Imágenes para el sitio web y las redes sociales
- Gráficos profesionales de alta calidad
- Adjuntar archivo de edición

Target:
- CEO
- CMO
- Emprendedor
- Gente relacionada con el marketing digital

Ideas iniciales de la portada:
- Minimalista
- Atemporal: Evitar gafas de realidad virtual (son productos que cambian con frecuencia)

Descripción del libro:
No se trata de un libro técnico sobre el metaverso. El objetivo del libro es llegar a marketers, CEOs, emprendedores, perfiles tecnológicos con visión de negocio que quieren descubrir cómo llevar su negocio o su idea de negocio al metaverso, y cómo aplicar modelos de negocio.

El libro se divide en un primer bloque de presentación del metaverso, introducción a la economía digital, y modelos de negocio aplicados al metaverso.

Ejemplos de portada:
- cover1: este formato es mi favorito, minimalista, atemporal y fácil de leer.
- cover2: esta portada me parece interesante por la cercanía con los colores habituales del metaverso.
- cover3: aunque con un toque retro (no es lo que busco), es un formato que me parece interesante por no recurrir a las gafas, y sin entrar en formato fotografía.
- cover4 y cover5: me gusta la relación de colores entre la letra y el fondo para dar prioridad al título.
- cover6: me gusta usar dos colores, en este caso para destacar metaverso, y la imagen de la portada te hace sentir más listo (por pensar diferente).

Título: "Rutas de empresa hacia lo intangible"

Texto asociado:
"Lidera la transición de tu negocio hacia el metaverso"

"Descubre los principales modelos de negocio del metaverso y cómo aplicarlos"

Autor: Tomàs Velabrun

```html
<!DOCTYPE html>
<html lang="es">
<head>
<meta charset="utf-8">
<title>Rutas de empresa hacia lo Intangible — Cubierta</title>
<link href="https://fonts.googleapis.com/css2?family=Oswald:wght@400;500;600&family=Open+Sans:wght@400;600&display=swap" rel="stylesheet">
<style>
  :root{
    --stage:#e3e0dc;
    --navy-deep:#0b1a33;
    --navy:#12305a;
    --blue:#1d4f8a;
    --cyan:#3fb6e8;
    --glow:#7fd8ff;
    --ink:#ffffff;
    --ink-soft:#d9e6f5;
  }
  *{box-sizing:border-box;margin:0;padding:0}
  html,body{width:1200px;height:800px;overflow:hidden;background:var(--stage)}
  .stage{position:relative;width:1200px;height:800px}
  .wrap{position:absolute;left:155px;top:80px;width:890px;height:640px;display:flex}
  .panel{position:relative;height:640px;overflow:hidden;
    background:linear-gradient(180deg,var(--navy-deep) 0%,var(--navy) 38%,var(--blue) 70%,var(--navy-deep) 100%)}
  .back,.front{width:420px}
  .spine{width:50px;background:linear-gradient(180deg,var(--navy-deep),var(--navy) 60%,var(--navy-deep));
    border-left:1px solid rgba(255,255,255,.08);border-right:1px solid rgba(255,255,255,.08)}
  .city-scene{position:absolute;left:0;right:0;bottom:0;height:360px;
    background:
      radial-gradient(ellipse at 55% 60%,rgba(127,216,255,.55),transparent 60%),
      linear-gradient(180deg,rgba(29,79,138,0) 0%,#1c5c9c 40%,#2a7fc0 62%,#0f2f5c 100%)}
  .front .city-scene{height:380px}
  .title-kicker{position:absolute;left:0;right:0;top:42px;text-align:center;
    font-family:"Oswald",sans-serif;font-weight:500;font-size:25px;letter-spacing:.5px;color:var(--ink)}
  .title-main{position:absolute;left:0;right:0;top:72px;text-align:center;
    font-family:"Oswald",sans-serif;font-weight:600;font-size:72px;line-height:1;letter-spacing:1px;color:var(--ink)}
  .tagline{position:absolute;left:40px;right:40px;top:172px;text-align:center;
    font-family:"Oswald",sans-serif;font-weight:500;font-size:16px;line-height:1.4;color:var(--ink)}
  .promise{position:absolute;left:40px;right:40px;top:222px;text-align:center;
    font-family:"Open Sans",sans-serif;font-size:16px;line-height:1.35;color:var(--ink-soft)}
  .author{position:absolute;left:0;right:0;bottom:26px;text-align:center;
    font-family:"Oswald",sans-serif;font-weight:400;font-size:18px;letter-spacing:6px;color:var(--ink)}
  .back .title-kicker{top:82px;font-size:22px}
  .back .title-main{top:108px;font-size:60px}
  .synopsis{position:absolute;left:34px;right:34px;top:218px;
    font-family:"Open Sans",sans-serif;font-size:13.5px;line-height:1.5;color:var(--ink)}
  .synopsis p+p{margin-top:14px}
  .spine-title,.spine-author{position:absolute;left:50%;writing-mode:vertical-rl;
    font-family:"Oswald",sans-serif;color:var(--ink);white-space:nowrap;transform:translateX(-50%)}
  .spine-title{top:22px;font-weight:500;font-size:17px;letter-spacing:.5px}
  .spine-author{bottom:22px;font-size:13px;letter-spacing:4px}
</style>
</head>
<body>
<div class="stage">
  <div class="wrap">
    <section class="panel back">
      <div class="city-scene" role="img" aria-label="Ciudad futurista nocturna iluminada en tonos azules y cian"></div>
      <h2 class="title-kicker">RUTAS DE EMPRESA HACIA LO</h2>
      <div class="title-main">INTANGIBLE</div>
      <div class="synopsis">
        <p>This is not a technical book about the metaverse. The objective of the book is to reach marketers, CEOs, entrepreneurs, technological profiles with business vision who want to discover how to take their business or business idea to the metaverse, and how to apply business models.</p>
        <p>The book is divided into a first block presenting the metaverse, an introduction to the digital economy, and business models applied to the metaverse.</p>
      </div>
    </section>
    <section class="panel spine">
      <div class="spine-title">RUTAS DE EMPRESA HACIA LO INTANGIBLE</div>
      <div class="spine-author">TOMÀS VELABRUN</div>
    </section>
    <section class="panel front">
      <div class="city-scene" role="img" aria-label="Hombre de espaldas en un mirador ante una ciudad futurista de luces azules"></div>
      <h1 class="title-kicker">RUTAS DE EMPRESA HACIA LO</h1>
      <div class="title-main">INTANGIBLE</div>
      <p class="tagline">LEAD THE TRANSITION OF YOUR BUSINESS<br>INTO THE METAVERSE</p>
      <p class="promise">Discover the main business models of the metaverse and how to apply them</p>
      <div class="author">TOMÀS VELABRUN</div>
    </section>
  </div>
</div>
</body>
</html>
```